Mango Grove Indian Restaurants 2019 Menu

Hi,
Please find attached menu text in pdf format. It contains 4 pages. Please work on the menu pages. I will further work with the winner to add the cover page and images as an extended project

Please visit www.mangogroveeats.com.au for more information

```html
<!DOCTYPE html>
<html lang="en">
<head>
<meta charset="utf-8">
<title>Mango Grove — Starters</title>
<link href="https://fonts.googleapis.com/css2?family=Abel&family=Barlow+Semi+Condensed:wght@600&family=Raleway:wght@300&display=swap" rel="stylesheet">
<style>
:root{
  --page:#ffffff;
  --panel:#fdf9f7;
  --orange:#e9a13b;
  --border:#f2b24a;
  --ink:#2b2b2b;
  --chilli:#d93a2b;
  --leaf:#4a9a3a;
  --blush:#f3c9cf;
  --brand:#c9362e;
}
*{margin:0;padding:0;box-sizing:border-box}
html,body{width:1200px;height:1200px;overflow:hidden;background:var(--page)}
.canvas{position:relative;width:1200px;height:1200px;background:var(--page)}
.menu-panel{position:absolute;left:0;top:192px;width:1200px;height:762px;background:var(--panel);
  border-top:3px solid var(--border);border-bottom:3px solid var(--border);overflow:hidden}
.side-border{position:absolute;top:0;width:26px;height:100%;
  background:repeating-linear-gradient(180deg,#f7c87a 0 18px,#fbe3bb 18px 36px)}
.side-border.left{left:0}.side-border.right{right:0}
.photo{position:absolute}
.photo.left{left:268px;top:0;width:190px;height:78px;background:linear-gradient(135deg,#3a4a2c,#c8b58a);border-radius:0 0 6px 6px}
.photo.main{left:458px;top:-10px;width:312px;height:190px;border-radius:0 0 160px 160px;
  background:radial-gradient(circle at 50% 40%,#7a2a1a,#b84a22 55%,#f2efe9 72%)}
.photo.right{left:770px;top:0;width:145px;height:84px;background:linear-gradient(135deg,#f0d6a0,#d9a85a);border-radius:0 0 6px 6px}
.splash{position:absolute;left:330px;top:40px;width:420px;height:180px;border-radius:50%;background:var(--blush);opacity:.55;filter:blur(6px)}
.chilli-art{position:absolute;left:1005px;top:35px;width:80px;height:85px;border-radius:40%;background:linear-gradient(90deg,#f6c9b8,#fbe6b9);opacity:.8}
.mandala{position:absolute;left:440px;top:520px;width:340px;height:340px;border-radius:50%;
  background:radial-gradient(circle,#f7e4e2 0,#fbf0ee 55%,transparent 70%);opacity:.8}
.title{position:absolute;left:64px;top:118px;font-family:'Raleway',sans-serif;font-weight:300;
  color:var(--orange);font-size:75px;line-height:66px;letter-spacing:1px}
.title span{display:block}
.title .second{padding-left:102px}
.column{position:absolute;color:var(--ink);font-family:'Abel',sans-serif}
.item{position:absolute;left:0;width:100%}
.item h3{font-family:'Barlow Semi Condensed',sans-serif;font-weight:600;font-size:11.5px;margin-bottom:14px;display:flex;align-items:center;gap:4px}
.item h3 small{font-family:'Abel',sans-serif;font-weight:400;font-size:10px}
.item p{font-size:10px;line-height:12.5px;text-align:justify}
.col-1 .item h3{font-size:12px}
.col-1 .item p{font-size:11.5px;line-height:12.5px}
.col-1{left:58px;top:0;width:234px;height:100%}
.col-2{left:334px;top:0;width:233px;height:100%}
.col-3{left:610px;top:0;width:250px;height:100%}
.col-4{left:890px;top:0;width:250px;height:100%}
.icon{width:11px;height:12px}
.brand{position:absolute;left:962px;top:692px;display:flex;align-items:center;gap:6px;
  font-family:'Barlow Semi Condensed',sans-serif;font-weight:600;font-size:22px;color:var(--brand)}
.brand i{display:block;width:14px;height:14px;background:var(--brand)}
</style>
</head>
<body>
<svg width="0" height="0" style="position:absolute">
  <symbol id="chilli" viewBox="0 0 12 12"><path d="M3 2 C5 5 6 8 4 11 C8 9 9 5 7 2 Z" fill="#d93a2b"/></symbol>
  <symbol id="leaf" viewBox="0 0 12 12"><path d="M1 10 C1 4 5 1 11 1 C11 7 7 11 1 10 Z" fill="#4a9a3a"/></symbol>
</svg>
<div class="canvas">
  <section class="menu-panel">
    <div class="side-border left" role="img" aria-label="Decorative ornamental border"></div>
    <div class="side-border right" role="img" aria-label="Decorative ornamental border"></div>
    <div class="splash" role="img" aria-label="Pink paint splash decoration"></div>
    <div class="photo left" role="img" aria-label="Photo of a spiced vegetable dish"></div>
    <div class="photo main" role="img" aria-label="Photo of a chilli-tossed starter in a white bowl"></div>
    <div class="photo right" role="img" aria-label="Photo of fried dumplings on a plate"></div>
    <div class="chilli-art" role="img" aria-label="Faint chilli illustration"></div>
    <div class="mandala" role="img" aria-label="Faint mandala pattern"></div>

    <h1 class="title"><span>STAR</span><span class="second">TERS</span></h1>

    <div class="column col-1">
      <div class="item" style="top:268px">
        <h3>65 (8 pcs) <small>DF, NF</small><svg class="icon"><use href="#chilli"/></svg><svg class="icon"><use href="#chilli"/></svg></h3>
        <p>Boneless Chicken or Gobi (cauliflower) pieces marinated in a home-made special masala mix and deep fried in spicy batter made with chickpea flour and exotic spices.<br>Gobi (Cauliflower) $8 | Chicken $14<br>Extra per piece Gobi (Cauliflower) $1 | Chicken $1.5</p>
      </div>
      <div class="item" style="top:420px">
        <h3>Chilli Dry (8 pcs) <small>DF, GF, NF</small><svg class="icon"><use href="#chilli"/></svg><svg class="icon"><use href="#chilli"/></svg><svg class="icon"><use href="#chilli"/></svg><svg class="icon"><use href="#leaf"/></svg></h3>
        <p>Battered and fried vegetables/meats/seafood smothered in, home-made sauce made with a variety of chillies, celery, cabbage, ginger, garlic, soy sauce, vinegar and exotic spices.<br>Gobi (Cauliflower) $12 extra per piece $1.5<br>Mushroom/Paneer (cheese) /Chicken $14 extra per piece $1.5<br>Fish/Prawn $20 &nbsp;Extra per piece $2.5</p>
      </div>
      <div class="item" style="top:580px">
        <h3>Manchurian Dry (8 pcs) <small>DF,GF, NF</small><svg class="icon"><use href="#chilli"/></svg><svg class="icon"><use href="#chilli"/></svg><svg class="icon"><use href="#chilli"/></svg><svg class="icon"><use href="#leaf"/></svg></h3>
        <p>Battered and fried vegetables/meats/seafood that are tossed in home-made saucemade with celery, cabbage, ginger, garlic, soy sauce, vinegar and exotic spices.<br>Gobi (Cauliflower) $12 extra per piece $1.5<br>Mushroom/Paneer (cheese) /Chicken $14 extra per piece $1.5<br>Fish/Prawn $20 Extra per piece $2.5</p>
      </div>
    </div>

    <div class="column col-2">
      <div class="item" style="top:294px">
        <h3>Onion Bhaji <small>DF,GF, NF</small><svg class="icon"><use href="#chilli"/></svg><svg class="icon"><use href="#chilli"/></svg><svg class="icon"><use href="#leaf"/></svg></h3>
        <p>Deep fried onions marinated in chickpea, rice and corn flour with exotic spices.<br>Small (5 pcs) $6 | Large (10 pcs) $10 Extra per piece $1</p>
      </div>
      <div class="item" style="top:388px">
        <h3>Pakora (8pcs) <small>DF,GF, NF</small><svg class="icon"><use href="#chilli"/></svg><svg class="icon"><use href="#leaf"/></svg></h3>
        <p>Deep fried pieces dipped in a mildly spiced chickpea &amp; corn flour batter mix.<br>Vegetables - Potato, Eggplant, Spinach, Gobi $6 -Extra per piece $0.50<br>Paneer (cheese) /Chicken $14 extra per piece $1.5<br>Fish/Prawn $20 Extra per piece $2.5</p>
      </div>
      <div class="item" style="top:520px">
        <h3>Potato Fries <small>DF,GF, NF</small><svg class="icon"><use href="#leaf"/></svg></h3>
        <p>Thin cut straight deep fried local potatoes.<br>Small $5 | Large $8</p>
      </div>
    </div>

    <div class="column col-3">
      <div class="item" style="top:293px">
        <h3>Palak Pakora <small>(8pcs) DF,GF, NF</small><svg class="icon"><use href="#chilli"/></svg><svg class="icon"><use href="#leaf"/></svg></h3>
        <p>Crisply fried spinach leaves dipped in mildly spiced chickpea batter topped with tangy chutneys, yoghurt, onion, tomato finished with sprinkles of mildly spiced crunchy chickpea noodles<br>$12. Extra per piece $1.50</p>
      </div>
      <div class="item" style="top:412px">
        <h3>Samosa <small>(2 pcs) NF</small><svg class="icon"><use href="#chilli"/></svg><svg class="icon"><use href="#chilli"/></svg></h3>
        <p>Deep fried, triangular, savoury pastry containing mildly spiced vegetables or meat filling. Standard serving contains 2 large pieces.<br>Vegetable $6 | Chicken $7 | Lamb $8<br>Extra per piece Vegetable $3 | Chicken $3.5 | Lamb $4</p>
      </div>
    </div>

    <div class="column col-4">
      <div class="item" style="top:232px">
        <h3>Samosa Chat <small>(3pcs) NF</small><svg class="icon"><use href="#chilli"/></svg><svg class="icon"><use href="#chilli"/></svg></h3>
        <p>Crushed vegetable samosa pieces topped with tangy chutneys, yoghurt, onion ,tomato finished with sprinkles of mildly spiced<br>crunchy chickpea noodles $12. Extra per piece $4</p>
      </div>
      <div class="item" style="top:337px">
        <h3>Seekh KebabT <small>(6pcs) DF,GF, NF</small><svg class="icon"><use href="#chilli"/></svg><svg class="icon"><use href="#chilli"/></svg></h3>
        <p>Lamb and chicken mince mixed with exotic spices, fresh coriander grilled on skewers in tandoor oven<br>$18 Extra per piece $3</p>
      </div>
      <div class="item" style="top:431px">
        <h3>Tandoori/Tikka <small>DF,GF, NF</small><svg class="icon"><use href="#chilli"/></svg><svg class="icon"><use href="#chilli"/></svg></h3>
        <p>Paneer (cheese)/chicken/seafood marinated in yoghurt and exotic spices roasted in tandoor oven<br>Lemon coriander boneless chicken / Paneer (cheese) 8 pcs $14 extra per piece $1.5<br>Chicken on bone ½ bird $ 10 ; whole bird $18<br>Fish /Prawn 8 pcs $20 ; extra per piece $2.5</p>
      </div>
      <div class="item" style="top:564px">
        <h3>Tossed Veggies <small>DF,GF, NF</small><svg class="icon"><use href="#chilli"/></svg><svg class="icon"><use href="#leaf"/></svg></h3>
        <p>Local fresh produce cauliflower, carrot, beans, peas, capsicum are blanched and tossed in oil with mildly fragrant spices.<br>Small bowl $5 | Large bowl $10</p>
      </div>
    </div>

    <div class="brand"><i></i>Mango Grove</div>
  </section>
</div>
</body>
</html>
```